Business Card for Childrens Book Publisher

Would like a business card that reflects a newly established boutique childrens publishing company. The first project is a book to help raise children's self esteem titled "We Dance Till Noon." To get a better idea of the type of look I am after go to te website www.Wedancetillnoon.example.au. You can take the images from the book and use them for the business card. Would like it to have a fun innovative look and feel to it. The business is about being uplifting and positive for children, but also creating beautiful, high quality books. You can use whatever images you see on the website but I have more high res files that I can send to you over drop box or some other programs if you need them.I would like the business card to be two sided.

The information on the business card is:

Marble Lantern Books
Greta Malloway
Publisher/Author

Marble Lantern Books
marble lanterns glowing bright
T 0491 356 207
Po Box 64, Fernhill Rise, Vic 3019, Australia
ABN: 36 517 904 128
gretamalloway@marblelanternbooks.example
www.marblelanternbooks.example

Target Market(s)

Booksellers, parents, schools, kindergartens, owners of children's boutiques, retailers.

Industry/Entity Type

Boutique

Requirements
Must have
• Would it to be double sided.

```html
<!DOCTYPE html>
<html lang="en">
<head>
<meta charset="utf-8">
<title>Marble Lantern Books – Business Card</title>
<link rel="stylesheet" href="https://fonts.googleapis.com/css2?family=Kalam:wght@300;400&family=Pinyon+Script&display=swap">
<style>
  :root {
    --paper: #ffffff;
    --ink: #111111;
    --name-blue: #1f3fe0;
    --rule: #555555;
    --star: #f2d54a;
    --star-edge: #c9a82a;
    --girl-shirt: #b9d39a;
    --girl-jeans: #7d97c4;
    --boy-shirt: #9cc86a;
    --dog-tan: #d99a55;
    --skin: #f3d9c2;
  }
  * { margin: 0; padding: 0; box-sizing: border-box; }
  html, body { width: 1200px; height: 1113px; overflow: hidden; background: var(--paper); }
  .canvas { position: relative; width: 1200px; height: 1113px; background: var(--paper); color: var(--ink); }

  .card { position: absolute; left: 0; width: 1021px; border-right: 2px solid var(--rule); }
  .card--front { top: 0; height: 588px; border-bottom: 2px solid var(--rule); }
  .card--back { top: 588px; height: 525px; }

  .side-label {
    position: absolute; font-family: Arial, Helvetica, sans-serif; font-size: 21px; color: var(--ink);
  }
  .side-label--front { left: 1075px; top: 230px; }
  .side-label--back { left: 1078px; top: 772px; }

  .brand {
    position: absolute; font-family: "Kalam", cursive; font-weight: 300;
    font-size: 76px; line-height: 1; white-space: nowrap; letter-spacing: 1px;
  }
  .card--front .brand { left: 40px; top: 42px; }
  .card--back .brand { left: 52px; top: 46px; font-size: 78px; }

  .illustration { position: absolute; border-radius: 40px; }
  .illustration--girl {
    left: 26px; top: 165px; width: 143px; height: 339px;
    background: linear-gradient(180deg, var(--skin) 0%, var(--skin) 22%, var(--girl-shirt) 35%, var(--girl-shirt) 58%, var(--girl-jeans) 62%, var(--girl-jeans) 90%, #e8eef2 100%);
  }
  .illustration--boy-dog {
    left: 765px; top: 261px; width: 214px; height: 148px;
    background: linear-gradient(90deg, var(--dog-tan) 0%, var(--dog-tan) 40%, var(--skin) 50%, var(--boy-shirt) 70%, #e05a3c 100%);
  }

  .person-name {
    position: absolute; left: 250px; top: 232px; font-family: "Pinyon Script", cursive;
    font-size: 84px; line-height: 1; color: var(--name-blue); white-space: nowrap;
  }
  .person-role {
    position: absolute; left: 466px; top: 334px; font-family: "Kalam", cursive;
    font-size: 20px; color: var(--name-blue); white-space: nowrap;
  }
  .front-web {
    position: absolute; left: 266px; top: 466px; font-family: "Kalam", cursive; font-weight: 300;
    font-size: 28px; letter-spacing: 2px; white-space: nowrap;
  }

  .details {
    position: absolute; left: 0; top: 198px; width: 1008px; list-style: none;
    font-family: "Kalam", cursive; font-weight: 300; font-size: 35px; line-height: 45px;
    letter-spacing: 3px; text-align: center;
  }
  .details li { white-space: nowrap; }
  .star { display: inline-block; width: 30px; height: 30px; vertical-align: -3px; }
  .star--lead { margin-right: 12px; }
  .star--trail { margin-left: 12px; vertical-align: -10px; }
</style>
</head>
<body>
<main class="canvas">
  <section class="card card--front" aria-label="Card front">
    <h1 class="brand">Marble Lantern Books</h1>
    <div class="illustration illustration--girl" role="img" aria-label="Book illustration of a little girl in a striped shirt looking up at a butterfly"></div>
    <p class="person-name">Greta Malloway</p>
    <p class="person-role">- Publisher and Author</p>
    <div class="illustration illustration--boy-dog" role="img" aria-label="Book illustration of a boy crouching to hug his dog"></div>
    <p class="front-web">www.marblelanternbooks.example</p>
  </section>

  <section class="card card--back" aria-label="Card back">
    <h2 class="brand">Marble Lantern Books</h2>
    <ul class="details">
      <li><svg class="star star--lead" viewBox="0 0 24 24" aria-hidden="true"><polygon points="12,1.5 15,9 23,9.3 16.8,14.2 19,22 12,17.5 5,22 7.2,14.2 1,9.3 9,9" fill="var(--star)" stroke="var(--star-edge)" stroke-width="1"/></svg>marble lanterns glowing bright</li>
      <li>T 0491 356 207</li>
      <li>Po Box 64 Fernhill Rise Vic 3019 Australia</li>
      <li>ABN 36 517 904 128</li>
      <li>gretamalloway@marblelanternbooks.example</li>
      <li>www.marblelanternbooks.example<svg class="star star--trail" viewBox="0 0 24 24" aria-hidden="true"><polygon points="12,1.5 15,9 23,9.3 16.8,14.2 19,22 12,17.5 5,22 7.2,14.2 1,9.3 9,9" fill="var(--star)" stroke="var(--star-edge)" stroke-width="1"/></svg></li>
    </ul>
  </section>

  <p class="side-label side-label--front">Front</p>
  <p class="side-label side-label--back">Back</p>
</main>
</body>
</html>
```